I need a better looking dashboard for my web application

I have a very table heavy web page that I would like to add a design touch to it. I have the logo and primary colors picked out, I just need some help in adding visual appeal the page. I would also like to add a couple of button to the page as shortcuts. Every spot that has a + sign could have a button added. I would also like to add another graph (the data will be in the uploaded files. Please feel free to ask any questions :-)

```html
<!DOCTYPE html>
<html lang="en">
<head>
<meta charset="utf-8">
<title>ShiftCover – Sub Management Dashboard</title>
<link href="https://fonts.googleapis.com/css2?family=Roboto:wght@400;500;700&display=swap" rel="stylesheet">
<style>
  :root{
    --bg:#e4f1f7;
    --card:#ffffff;
    --line:#e2e2ea;
    --sep:#d6d6e0;
    --head:#ddd1f6;
    --head-text:#6a4fb0;
    --purple:#6b4ea8;
    --teal:#27a9d3;
    --teal-light:#5fd3f2;
    --lavender:#e0d4f7;
    --green:#2fa84f;
    --text:#3c3c44;
    --title:#2b2b33;
    --donut-dark:#2a85c8;
    --donut-mid:#5db5ee;
    --donut-light:#8fd0f8;
  }
  *{box-sizing:border-box;margin:0;padding:0}
  html,body{width:1200px;height:801px;overflow:hidden}
  body{font-family:'Roboto',sans-serif;background:linear-gradient(135deg,#eaf6fa 0%,var(--bg) 60%,#dfeef6 100%);position:relative;color:var(--text)}
  .abs{position:absolute}
  .app{left:18px;top:15px;width:1163px;height:712px;background:var(--card);box-shadow:0 2px 10px rgba(40,80,120,.08)}
  .topbar{left:29px;top:23px;width:1142px;height:25px;border:1px solid var(--line);border-radius:4px;background:#fff}
  .brand{left:46px;top:27px;display:flex;align-items:center;gap:5px;font-size:13px;font-weight:500;color:#2f8fd1}
  .brand-dot{width:10px;height:10px;border-radius:50%;background:var(--purple)}
  .page-title{left:191px;top:26px;font-size:15px;font-weight:700;color:#2c9fd6;letter-spacing:.3px}
  .nav{right:36px;top:31px;display:flex;gap:12px;font-size:7px;color:#333;align-items:center}
  .nav span{display:flex;align-items:center;gap:3px}
  .nav svg{width:8px;height:8px;fill:var(--purple)}
  .tab{top:64px;width:78px;height:20px;border-radius:3px;font-size:7.5px;font-weight:500;display:flex;align-items:center;justify-content:center;letter-spacing:.3px}
  .tab.active{left:30px;background:var(--teal);color:#fff}
  .tab.plain{left:111px;border:1px solid var(--teal);color:#2a7fae;background:#f3fbfe}
  .section-title{font-size:12.5px;font-weight:500;color:var(--title)}
  .grid{display:grid;align-items:center}
  .table{border:1px solid var(--line);background:#fff}
  .thead{background:var(--head);color:var(--head-text);font-size:8.5px;font-weight:500;text-transform:uppercase}
  .row{height:31.4px;border-bottom:1px solid var(--line);font-size:8.5px}
  .row:last-child{border-bottom:none}
  .c{height:20px;display:flex;align-items:center;padding-left:16px;white-space:nowrap;overflow:hidden}
  .c+.c{border-left:1px solid var(--sep)}
  .c.center{justify-content:center;padding-left:0}
  .c.tight{line-height:1;flex-direction:column;align-items:flex-start;justify-content:center;padding-left:9px;font-size:8px}
  .add-btn{background:var(--purple);color:#fff;font-size:8.5px;font-weight:500;width:37px;height:18px;border-radius:3px;display:flex;align-items:center;justify-content:center;margin-left:12px}
  .icons{display:flex;gap:15px;padding-left:14px}
  .icons svg{width:9px;height:9px;fill:#333}
  .avatar{width:16px;height:16px;border-radius:50%;background:radial-gradient(circle at 50% 40%,#d9967a,#8a3f2e);margin-right:4px;flex:none}
  .avatar.alt{background:radial-gradient(circle at 50% 40%,#b9c4a2,#4b5a3c)}
  .caret{width:0;height:0;border-left:3px solid transparent;border-right:3px solid transparent;border-top:3px solid #222}
  .scroll{height:3px;background:#f0e8ee;border-radius:2px}
  .scroll i{position:absolute;left:93px;width:35px;height:3px;background:#d9ccf5;border-radius:2px}
  .box{border:1px solid var(--line);background:#fff}
  .legend{display:flex;gap:9px;font-size:10px;color:#333;align-items:center}
  .legend span{display:flex;align-items:center;gap:5px}
  .legend i{width:7px;height:7px;border-radius:50%;display:inline-block}
  .outline-btn{width:88px;height:20px;border:1px solid var(--teal);border-radius:3px;color:#2a7fae;font-size:7.5px;font-weight:500;display:flex;align-items:center;justify-content:center;background:#fff}
  .sum-table{border:1px solid #d8d8de}
  .sum-table .r{height:26.5px;border-top:1px solid #d8d8de;display:grid;grid-template-columns:131px 1fr;align-items:center;font-size:9.5px;font-weight:500;color:#222}
  .sum-table .r:first-child{border-top:none}
  .sum-table .r div{padding-left:18px;height:100%;display:flex;align-items:center}
  .sum-table .r div+div{border-left:1px solid #d8d8de;padding-left:20px}
  .donut-label{font-size:9px;color:#666;line-height:1.25}
  .footer{left:171px;top:767px;width:857px;height:40px;background:var(--teal);border-radius:34px 34px 0 0;color:#fff;font-size:10.5px;display:flex;justify-content:center;padding-top:11px;gap:6px}
  .pp .thead{font-size:6.5px}
  .pp .row{height:24.8px;font-size:7px}
  .pp .c{padding-left:8px;height:16px}
  .thumb{width:18px;height:14px;background:linear-gradient(135deg,#b8323c,#5a1e2a);margin-left:6px}
  .link{color:#2a8fd0;font-size:6.5px;font-weight:500}
  .opt{display:flex;gap:4px;padding-left:10px}
  .opt span{width:14px;height:14px;border-radius:50%;display:flex;align-items:center;justify-content:center}
  .opt svg{width:7px;height:7px;stroke:#fff;stroke-width:2.4;fill:none}
</style>
</head>
<body>
<svg width="0" height="0" style="position:absolute">
  <symbol id="i-edit" viewBox="0 0 16 16"><path d="M11.5 1.5l3 3-9 9-3.8.8.8-3.8z"/></symbol>
  <symbol id="i-trash" viewBox="0 0 16 16"><path d="M5 1h6v1.5h3.5V4h-13V2.5H5zM2.8 5h10.4l-.9 10H3.7z"/></symbol>
</svg>

<div class="abs app"></div>
<div class="abs topbar"></div>
<div class="abs brand"><span class="brand-dot"></span>ShiftCover</div>
<div class="abs page-title">Sub Management</div>
<nav class="abs nav">
  <span><svg viewBox="0 0 16 16"><path d="M8 1l7 7h-2v7h-4v-5H7v5H3V8H1z"/></svg>Home</span>
  <span><svg viewBox="0 0 16 16"><path d="M1 2h14v10H9v2h2v1H5v-1h2v-2H1zm2 2v6h10V4z"/></svg>Demo Outbox</span>
  <span><svg viewBox="0 0 16 16"><path d="M1 3l4-1.5 6 2 4-1.5v11l-4 1.5-6-2L1 14z"/></svg>Location Admin</span>
  <span><svg viewBox="0 0 16 16"><circle cx="8" cy="5" r="3.5"/><path d="M1.5 15c0-4 3-6 6.5-6s6.5 2 6.5 6z"/></svg>Regular Staff <span class="caret" style="margin-left:2px"></span></span>
  <span><svg viewBox="0 0 16 16"><path d="M1 3h14v10H1zm1.5 1.5v.6L8 9l5.5-3.9v-.6z"/></svg>desk.lead@example.com</span>
</nav>

<div class="abs tab active">DASHBOARD</div>
<div class="abs tab plain">CALENDAR</div>

<!-- Managed Openings -->
<h2 class="abs section-title" style="left:34px;top:100px">Managed Openings</h2>
<div class="abs table" style="left:34px;top:123px;width:562px">
  <div class="grid thead" style="grid-template-columns:65px 75px 97px 66px 82px 62px 1fr;height:32px">
    <div class="c" style="padding-left:0"><span class="add-btn">ADD</span></div>
    <div class="c">Category</div><div class="c">Regular Staff</div><div class="c">Status</div>
    <div class="c" style="padding-left:9px">Summary&nbsp;<svg width="8" height="9" viewBox="0 0 8 9"><path d="M4 9V1M1 4l3-3 3 3" stroke="#222" fill="none" stroke-width="1"/></svg></div>
    <div class="c">Location</div><div class="c">Time Slots Summary</div>
  </div>
  <div class="grid row" style="grid-template-columns:65px 75px 97px 66px 82px 62px 1fr">
    <div class="c">Clear</div><div class="c"></div><div class="c"></div><div class="c" style="justify-content:flex-end;padding-right:16px"><span class="caret"></span></div><div class="c"></div><div class="c"></div><div class="c"></div>
  </div>
  <div class="grid row" style="grid-template-columns:65px 75px 97px 66px 82px 62px 1fr"><div class="c icons"><svg><use href="#i-edit"/></svg><svg><use href="#i-trash"/></svg></div><div class="c">Food Service</div><div class="c">Extra Duty</div><div class="c">Assigned</div><div class="c tight">Immediate Need!<br>Libra</div><div class="c center">LJE</div><div class="c">12/30-01/01 (2h 30m)</div></div>
  <div class="grid row" style="grid-template-columns:65px 75px 97px 66px 82px 62px 1fr"><div class="c icons"><svg><use href="#i-edit"/></svg><svg><use href="#i-trash"/></svg></div><div class="c">Teacher</div><div class="c"><span class="avatar" role="img" aria-label="Staff profile photo"></span>Leah Corbin</div><div class="c">Available</div><div class="c tight">Immediate Need!<br>Libra</div><div class="c center">LJE</div><div class="c">12/30-01/01 (2h 30m)</div></div>
  <div class="grid row" style="grid-template-columns:65px 75px 97px 66px 82px 62px 1fr"><div class="c icons"><svg><use href="#i-edit"/></svg><svg><use href="#i-trash"/></svg></div><div class="c">Food Service</div><div class="c">Extra Duty</div><div class="c">Assigned</div><div class="c tight">Immediate Need!<br>Libra</div><div class="c center">LJE</div><div class="c">12/30-01/01 (2h 30m)</div></div>
  <div class="grid row" style="grid-template-columns:65px 75px 97px 66px 82px 62px 1fr"><div class="c icons"><svg><use href="#i-edit"/></svg><svg><use href="#i-trash"/></svg></div><div class="c">Food Service</div><div class="c">Extra Duty</div><div class="c">Available</div><div class="c tight">Immediate Need!<br>Libra</div><div class="c center">LJE</div><div class="c">12/30-01/01 (2h 30m)</div></div>
  <div class="grid row" style="grid-template-columns:65px 75px 97px 66px 82px 62px 1fr"><div class="c icons"><svg><use href="#i-edit"/></svg><svg><use href="#i-trash"/></svg></div><div class="c">Teacher</div><div class="c"><span class="avatar" role="img" aria-label="Staff profile photo"></span>Leah Corbin</div><div class="c">Assigned</div><div class="c tight">Immediate Need!<br>Libra</div><div class="c center">LJE</div><div class="c">12/30-01/01 (2h 30m)</div></div>
  <div class="grid row" style="grid-template-columns:65px 75px 97px 66px 82px 62px 1fr"><div class="c icons"><svg><use href="#i-edit"/></svg><svg><use href="#i-trash"/></svg></div><div class="c">Food Service</div><div class="c">Extra Duty</div><div class="c">Available</div><div class="c tight">Immediate Need!<br>Libra</div><div class="c center">LJE</div><div class="c">12/30-01/01 (2h 30m)</div></div>
</div>
<div class="abs scroll" style="left:36px;top:390px;width:560px"><i></i></div>

<!-- Leave Requests -->
<h2 class="abs section-title" style="left:34px;top:410px">Regular Staff Leave Requests</h2>
<div class="abs table" style="left:34px;top:433px;width:562px">
  <div class="grid thead" style="grid-template-columns:65px 75px 97px 209px 1fr;height:42px">
    <div class="c" style="padding-left:0"><span class="add-btn">ADD</span></div>
    <div class="c">Status</div><div class="c">Full Name</div>
    <div style="height:42px;border-left:1px solid var(--sep);display:grid;grid-template-rows:1fr 1fr">
      <div style="display:flex;align-items:flex-end;justify-content:center;border-bottom:1px solid #c9bdea;padding-bottom:3px">Opening</div>
      <div style="display:flex;align-items:center;padding-left:16px;gap:56px"><span>Asignment</span><span>Prearranged Sub</span></div>
    </div>
    <div class="c">Time Slots Summary</div>
  </div>
  <div class="grid row" style="grid-template-columns:65px 75px 97px 91px 118px 1fr">
    <div class="c">Clear</div><div class="c" style="justify-content:flex-end;padding-right:12px"><span class="caret"></span></div><div class="c"></div><div class="c"></div><div class="c"></div><div class="c"></div>
  </div>
  <div class="grid row" style="grid-template-columns:65px 75px 97px 91px 118px 1fr"><div class="c icons"><svg><use href="#i-edit"/></svg><svg><use href="#i-trash"/></svg></div><div class="c">Pending</div><div class="c"><span class="avatar" role="img" aria-label="Staff profile photo"></span>Owen Pratt</div><div class="c">N/A</div><div class="c" style="padding-left:31px">Administrator</div><div class="c">12/30-01/01 (2h 30m)</div></div>
  <div class="grid row" style="grid-template-columns:65px 75px 97px 91px 118px 1fr"><div class="c icons"><svg><use href="#i-edit"/></svg><svg><use href="#i-trash"/></svg></div><div class="c">Pending</div><div class="c"><span class="avatar" role="img" aria-label="Staff profile photo"></span>Leah Corbin</div><div class="c">N/A</div><div class="c" style="padding-left:31px">N/A</div><div class="c">12/30-01/01 (2h 30m)</div></div>
  <div class="grid row" style="grid-template-columns:65px 75px 97px 91px 118px 1fr"><div class="c icons"><svg><use href="#i-edit"/></svg><svg><use href="#i-trash"/></svg></div><div class="c">Pending</div><div class="c"><span class="avatar" role="img" aria-label="Staff profile photo"></span>Extra Duty</div><div class="c">Counselor</div><div class="c" style="padding-left:31px">N/A</div><div class="c">12/30-01/01 (2h 30m)</div></div>
  <div class="grid row" style="grid-template-columns:65px 75px 97px 91px 118px 1fr"><div class="c icons"><svg><use href="#i-edit"/></svg><svg><use href="#i-trash"/></svg></div><div class="c">Pending</div><div class="c"><span class="avatar" role="img" aria-label="Staff profile photo"></span>Rita Salas</div><div class="c">N/A</div><div class="c"></div><div class="c">12/30-01/01 (2h 30m)</div></div>
  <div class="grid row" style="grid-template-columns:65px 75px 97px 91px 118px 1fr"><div class="c icons"><svg><use href="#i-edit"/></svg><svg><use href="#i-trash"/></svg></div><div class="c">Pending</div><div class="c"><span class="avatar" role="img" aria-label="Staff profile photo"></span>Leah Corbin</div><div class="c">Administrator</div><div class="c" style="padding-left:31px">N/A</div><div class="c">12/30-01/01 (2h 30m)</div></div>
  <div class="grid row" style="grid-template-columns:65px 75px 97px 91px 118px 1fr"><div class="c icons"><svg><use href="#i-edit"/></svg><svg><use href="#i-trash"/></svg></div><div class="c">Pending</div><div class="c"><span class="avatar" role="img" aria-label="Staff profile photo"></span>Dana Whitfield</div><div class="c">Administrator</div><div class="c" style="padding-left:20px"><span class="avatar alt" role="img" aria-label="Substitute profile photo"></span>&nbsp;Cole Ashby</div><div class="c">12/30-01/01 (2h 30m)</div></div>
</div>
<div class="abs scroll" style="left:36px;top:709px;width:560px"><i></i></div>

<!-- Location Overview -->
<h2 class="abs section-title" style="left:610px;top:100px">Location Overview</h2>
<div class="abs box" style="left:610px;top:123px;width:248px;height:147px">
  <svg width="248" height="147" viewBox="0 0 248 147" style="position:absolute;left:0;top:0">
    <text x="124" y="27" text-anchor="middle" font-family="Roboto,sans-serif" font-size="10" font-weight="500" fill="#2b2b33">Leave Requests/Openings/Assignments</text>
    <g stroke="#eee" stroke-width=".5">
      <line x1="8" y1="48" x2="242" y2="48"/><line x1="8" y1="60.2" x2="242" y2="60.2"/><line x1="8" y1="72.4" x2="242" y2="72.4"/><line x1="8" y1="84.6" x2="242" y2="84.6"/><line x1="8" y1="96.8" x2="242" y2="96.8"/>
    </g>
    <line x1="8" y1="109" x2="242" y2="109" stroke="#bbb" stroke-width=".6"/>
    <line x1="8" y1="46" x2="8" y2="109" stroke="#bbb" stroke-width=".6"/>
    <g font-family="Roboto,sans-serif" font-size="3" fill="#777" text-anchor="end">
      <text x="6" y="49">10</text><text x="6" y="61">8</text><text x="6" y="73">6</text><text x="6" y="85">4</text><text x="6" y="98">2</text><text x="6" y="110">0</text>
    </g>
    <rect x="21" y="90.7" width="25" height="18.3" fill="var(--purple)"/>
    <rect x="21" y="84.6" width="25" height="6.1" fill="var(--green)"/>
    <rect x="51" y="84.6" width="24" height="24.4" fill="var(--teal)"/>
    <rect x="99" y="78.5" width="25" height="30.5" fill="var(--purple)"/>
    <rect x="128" y="84.6" width="25" height="24.4" fill="var(--teal)"/>
    <rect x="175" y="72.4" width="25" height="36.6" fill="var(--purple)"/>
    <rect x="206" y="48" width="24" height="61" fill="var(--teal)"/>
    <g font-family="Roboto,sans-serif" font-size="2.6" fill="#666" text-anchor="middle">
      <text x="48" y="114">North Elementary</text><text x="126" y="114">Central Middle School</text><text x="203" y="114">West Middle School</text>
    </g>
    <g font-family="Roboto,sans-serif" font-size="2.6" fill="#555">
      <rect x="72" y="118" width="3" height="3" fill="var(--purple)"/><text x="76.5" y="120.6">Openings: Unfilled</text>
      <rect x="105" y="118" width="3" height="3" fill="var(--green)"/><text x="109.5" y="120.6">Openings: Filled</text>
      <rect x="136" y="118" width="3" height="3" fill="var(--teal)"/><text x="140.5" y="120.6">LeaveRequests: Pending</text>
    </g>
  </svg>
</div>

<!-- Pending Profile Images -->
<h2 class="abs section-title" style="left:872px;top:100px">Pending Profile Images</h2>
<div class="abs table pp" style="left:872px;top:123px;width:288px;height:147px">
  <div class="grid thead" style="grid-template-columns:57px 58px 118px 1fr;height:41px">
    <div class="c">First Name</div><div class="c">Last Name</div>
    <div style="height:41px;border-left:1px solid var(--sep);display:grid;grid-template-rows:1fr 1fr">
      <div style="display:flex;align-items:center;justify-content:center;border-bottom:1px solid #c9bdea">Profile Images</div>
      <div style="display:grid;grid-template-columns:50px 1fr;align-items:center;font-size:5px"><span style="text-align:center">Pending</span><span style="border-left:1px solid var(--sep);padding-left:7px">Previously Verified</span></div>
    </div>
    <div class="c" style="padding-left:14px">Options</div>
  </div>
  <div class="grid row" style="grid-template-columns:57px 58px 50px 68px 1fr"><div class="c">Harlow</div><div class="c">Jin</div><div class="c"><span class="thumb" role="img" aria-label="Pending profile photo"></span></div><div class="c link">None Available</div><div class="c opt"><span style="background:var(--teal)"><svg viewBox="0 0 8 8"><path d="M1.5 4.2l1.7 1.7L6.5 2.3"/></svg></span><span style="background:var(--purple)"><svg viewBox="0 0 8 8"><path d="M2 2l4 4M6 2L2 6"/></svg></span></div></div>
  <div class="grid row" style="grid-template-columns:57px 58px 50px 68px 1fr"><div class="c">Brooks</div><div class="c">Evan</div><div class="c"><span class="thumb" role="img" aria-label="Pending profile photo"></span></div><div class="c link">None Available</div><div class="c opt"><span style="background:var(--teal)"><svg viewBox="0 0 8 8"><path d="M1.5 4.2l1.7 1.7L6.5 2.3"/></svg></span><span style="background:var(--purple)"><svg viewBox="0 0 8 8"><path d="M2 2l4 4M6 2L2 6"/></svg></span></div></div>
  <div class="grid row" style="grid-template-columns:57px 58px 50px 68px 1fr"><div class="c">Harlow</div><div class="c">Jin</div><div class="c"><span class="thumb" role="img" aria-label="Pending profile photo"></span></div><div class="c link">None Available</div><div class="c opt"><span style="background:var(--teal)"><svg viewBox="0 0 8 8"><path d="M1.5 4.2l1.7 1.7L6.5 2.3"/></svg></span><span style="background:var(--purple)"><svg viewBox="0 0 8 8"><path d="M2 2l4 4M6 2L2 6"/></svg></span></div></div>
  <div class="grid row" style="grid-template-columns:57px 58px 50px 68px 1fr"><div class="c">Brooks</div><div class="c">Evan</div><div class="c"><span class="thumb" role="img" aria-label="Pending profile photo"></span></div><div class="c link">None Available</div><div class="c opt"><span style="background:var(--teal)"><svg viewBox="0 0 8 8"><path d="M1.5 4.2l1.7 1.7L6.5 2.3"/></svg></span><span style="background:var(--purple)"><svg viewBox="0 0 8 8"><path d="M2 2l4 4M6 2L2 6"/></svg></span></div></div>
  <div class="abs" style="left:4px;bottom:1px;width:278px;height:2px;background:#eee;border-radius:1px"><i style="position:absolute;left:84px;width:115px;height:2px;background:#d9ccf5"></i></div>
</div>

<!-- Summary panel -->
<div class="abs box" style="left:610px;top:281px;width:562px;height:431px"></div>
<div class="abs box" style="left:620px;top:293px;width:541px;height:128px"></div>
<h2 class="abs section-title" style="left:632px;top:320px;font-size:13px">Today’s Summary</h2>
<div class="abs legend" style="left:632px;top:352px">
  <span><i style="background:var(--purple)"></i>Unfilled</span>
  <span><i style="background:var(--teal)"></i>Filled</span>
  <span><i style="background:var(--lavender)"></i>No Sub Needed</span>
  <span><i style="background:var(--teal-light)"></i>Total</span>
</div>
<div class="abs" style="left:632px;top:378px;width:284px;height:11px;border-radius:6px;overflow:hidden;display:flex">
  <div style="width:45px;background:var(--purple)"></div>
  <div style="width:110px;background:var(--teal);border-radius:0 6px 6px 0;position:relative;z-index:2"></div>
  <div style="width:96px;background:var(--lavender);margin-left:-6px;border-radius:0 6px 6px 0;position:relative;z-index:1;padding-left:6px"></div>
  <div style="flex:1;background:var(--teal-light);margin-left:-6px"></div>
</div>
<div class="abs outline-btn" style="left:965px;top:342px">CREATE ABSENCE</div>
<div class="abs outline-btn" style="left:1061px;top:342px">APPROVE 8</div>
<div class="abs outline-btn" style="left:965px;top:369px">CREATE VACCANCY</div>
<div class="abs outline-btn" style="left:1061px;top:369px">APPROVE 3</div>

<div class="abs box" style="left:620px;top:431px;width:541px;height:262px"></div>
<div class="abs box" style="left:630px;top:440px;width:288px;height:201px"></div>
<h2 class="abs section-title" style="left:640px;top:470px;font-size:13px">Monthly Summary</h2>
<div class="abs sum-table" style="left:640px;top:503px;width:268px">
  <div class="r"><div></div><div style="border-left:none"></div></div>
  <div class="r"><div>Total Jobs</div><div>45</div></div>
  <div class="r"><div>Filled Jobs</div><div>data</div></div>
  <div class="r"><div>No Sub Needed</div><div>data</div></div>
</div>

<div class="abs box" style="left:925px;top:440px;width:230px;height:201px"></div>
<h2 class="abs section-title" style="left:945px;top:470px;font-size:13px">Monthly Summary</h2>
<svg class="abs" style="left:1003px;top:515px" width="82" height="82" viewBox="0 0 82 82">
  <g transform="rotate(-90 41 41)" fill="none" stroke-width="22">
    <circle cx="41" cy="41" r="30" stroke="var(--donut-dark)" stroke-dasharray="75.4 188.5"/>
    <circle cx="41" cy="41" r="30" stroke="var(--donut-mid)" stroke-dasharray="62.2 188.5" stroke-dashoffset="-75.4"/>
    <circle cx="41" cy="41" r="30" stroke="var(--donut-light)" stroke-dasharray="50.9 188.5" stroke-dashoffset="-137.6"/>
  </g>
</svg>
<div class="abs donut-label" style="left:978px;top:502px">No Sub<br>27%</div>
<div class="abs donut-label" style="left:1089px;top:526px">Filled<br>40%</div>
<div class="abs donut-label" style="left:1010px;top:598px">Open<br>33%</div>

<footer class="abs footer">© 2025 Companyname.All Rights Reserved <span>|</span> Privacy Policy <span>|</span> Terms of use</footer>
</body>
</html>
```